Lone Prairie Canvas & Sound Jubilee

Organization:
Lone Prairie Canvas and Sound Jubilee is a non-profit organization created by a group of anonymous donors to bring more fun, culture, and art to a small Texas town. Our mission is to promote art and music in Washington County.
The multi-day eclectic festival will feature three stages, a film, art vendors, live mural artists, and food trucks set up throughout historic downtown Brenham. The event is FREE to the public.
Goals:
We need an attractive poster to publicize the festival.
Details:
Lone Prairie Canvas and Sound Jubilee
Friday, October 14 – 16
Free admission (VIP tickets available)
Live music- 3 stages/10 bands
Film Screening
Art vendors and art walk
Live art murals
Food trucks
www.loneprairiecanvasandsoundjubilee.example
#loneprairiecanvasandsound
Requirements:
Please incorporate our festival logo attached.
Conclusion:
After selecting a poster design, we hope to continue to work with the artist to design other event materials including website splash page and rack cards using design elements from the poster.

```html
<!DOCTYPE html>
<html lang="en">
<head>
<meta charset="utf-8">
<title>Lone Prairie Canvas &amp; Sound Jubilee</title>
<link rel="stylesheet" href="https://fonts.googleapis.com/css2?family=Cinzel:wght@700;900&family=Oswald:wght@500;600&family=Raleway:wght@500;800&family=Dosis:wght@600&display=swap">
<style>
  :root {
    --gold-light: #fff3c4;
    --gold: #f7c948;
    --amber: #e8962a;
    --orange: #d9601a;
    --crimson: #8f1414;
    --wine: #5a0b0d;
    --ink: #1a0c0c;
    --cream: #fbf1d3;
    --white: #ffffff;
    --yellow: #ffe62e;
  }
  * { margin: 0; padding: 0; box-sizing: border-box; }
  html, body { width: 776px; height: 1200px; overflow: hidden; }
  body { background: var(--wine); }

  .poster {
    position: relative;
    width: 776px;
    height: 1200px;
    overflow: hidden;
    background: linear-gradient(180deg, var(--gold-light) 0%, #f9dc8a 22%, var(--amber) 45%, var(--orange) 60%, var(--crimson) 78%, var(--wine) 100%);
  }

  .crowd-photo {
    position: absolute;
    left: 0; top: 430px;
    width: 776px; height: 520px;
    background:
      radial-gradient(ellipse 60% 40% at 45% 20%, rgba(255,230,150,.55), transparent 70%),
      linear-gradient(180deg, transparent 0%, rgba(60,15,10,.55) 35%, rgba(40,8,8,.75) 70%, rgba(90,11,13,.2) 100%);
  }

  .date-badge {
    position: absolute;
    left: 195px; top: 30px;
    width: 392px; height: 100px;
    background: linear-gradient(180deg, #3a2222, var(--ink));
    border-radius: 12px;
    transform: rotate(-2deg);
    box-shadow: 0 6px 14px rgba(0,0,0,.35);
    text-align: center;
    color: var(--white);
    white-space: nowrap;
  }
  .date-badge .days {
    display: block;
    padding-top: 10px;
    font-family: 'Oswald', sans-serif; font-weight: 500;
    font-size: 20px; letter-spacing: 3px; line-height: 26px;
  }
  .date-badge .dates {
    display: block;
    font-family: 'Raleway', sans-serif; font-weight: 800;
    font-size: 36px; line-height: 44px;
  }
  .date-badge .dates sup { font-size: 17px; vertical-align: 14px; line-height: 0; }
  .date-badge .month { font-weight: 500; }

  .festival-name {
    position: absolute;
    left: 602px; top: 40px;
    width: 160px;
    display: flex; align-items: center; gap: 8px;
    font-family: 'Oswald', sans-serif; font-weight: 500;
    font-size: 14px; line-height: 17px; color: var(--ink);
  }
  .festival-name .dot { flex: none; width: 14px; height: 14px; border-radius: 50%; background: var(--ink); }

  .diamond {
    position: absolute;
    left: 218px; top: 200px;
    width: 340px; height: 340px;
    background: linear-gradient(135deg, #fffbe9, var(--cream));
    border-radius: 30px;
    transform: rotate(45deg);
    box-shadow: 0 0 40px rgba(255,255,230,.6);
  }

  .title {
    position: absolute;
    left: 0; top: 148px; width: 776px;
    text-align: center;
    font-family: 'Cinzel', serif; font-weight: 900;
    color: var(--crimson);
    text-shadow: 2px 3px 0 var(--wine), 0 6px 12px rgba(0,0,0,.3);
    line-height: 1;
    white-space: nowrap;
  }
  .title .line-1 { display: block; font-size: 64px; }
  .title .line-2 { display: block; font-size: 100px; }
  .title .line-3 { display: block; font-size: 116px; }

  .title-banner {
    position: absolute;
    left: 205px; top: 458px;
    width: 376px; height: 76px;
  }
  .title-banner span {
    position: absolute; inset: 0;
    display: flex; align-items: center; justify-content: center;
    font-family: 'Cinzel', serif; font-weight: 700;
    font-size: 52px; color: var(--cream);
  }

  .highlights {
    position: absolute;
    left: 104px; top: 728px;
    list-style: none;
    font-family: 'Oswald', sans-serif; font-weight: 500;
    font-size: 41px; line-height: 48px;
    color: var(--white);
    text-transform: uppercase;
    white-space: nowrap;
  }
  .highlights li::before { content: "•"; display: inline-block; width: 36px; }

  .admission {
    position: absolute;
    left: 0; top: 984px; width: 776px;
    text-align: center;
    color: var(--gold);
    font-family: 'Raleway', sans-serif;
    line-height: 1;
  }
  .admission .free { font-size: 42px; }
  .admission .free b { font-weight: 800; }
  .admission .free span { font-weight: 500; }
  .admission .vip { display: block; font-size: 20px; font-weight: 500; }

  .hashtag {
    position: absolute;
    left: 170px; top: 1062px;
    width: 436px; height: 38px;
    background: var(--yellow);
    display: flex; align-items: center; justify-content: center;
    font-family: 'Oswald', sans-serif; font-weight: 600;
    font-size: 24px; color: var(--ink);
    text-transform: uppercase;
    white-space: nowrap;
  }

  .website {
    position: absolute;
    left: 78px; top: 1104px;
    width: 620px; height: 58px;
    border: 2px solid var(--white);
    display: flex; align-items: center; justify-content: center;
    font-family: 'Dosis', sans-serif; font-weight: 600;
    font-size: 30px; color: var(--white);
    white-space: nowrap;
    overflow: hidden;
  }
</style>
</head>
<body>
<main class="poster">
  <div class="crowd-photo" role="img" aria-label="Festival crowd with raised hands silhouetted against warm stage lights"></div>

  <div class="date-badge">
    <span class="days">FRIDAY-SUNDAY</span>
    <span class="dates">14<sup>TH</sup>-16<sup>TH</sup> <span class="month">OCTOBER</span></span>
  </div>

  <div class="festival-name"><span class="dot"></span><span>Lone Prairie Canvas &amp; Sound Jubilee</span></div>

  <div class="diamond"></div>

  <h1 class="title">
    <span class="line-1">LONE PRAIRIE</span>
    <span class="line-2">CANVAS&amp;</span>
    <span class="line-3">SOUND</span>
  </h1>

  <div class="title-banner">
    <svg width="376" height="76" viewBox="0 0 376 76" aria-hidden="true">
      <defs>
        <linearGradient id="bannerFill" x1="0" y1="0" x2="0" y2="1">
          <stop offset="0" stop-color="#a81c1c"/>
          <stop offset="1" stop-color="#5a0b0d"/>
        </linearGradient>
      </defs>
      <path d="M8 0 H368 V26 A12 12 0 0 0 368 50 V76 H8 V50 A12 12 0 0 0 8 26 Z" fill="url(#bannerFill)"/>
      <rect x="30" y="10" width="316" height="56" fill="none" stroke="#fbf1d3" stroke-width="2" opacity=".5"/>
    </svg>
    <span>JUBILEE</span>
  </div>

  <ul class="highlights">
    <li>Live music- 3 stages / 10 bands</li>
    <li>Film screening</li>
    <li>Art vendors and art walk</li>
    <li>Live art murals</li>
    <li>Food trucks</li>
  </ul>

  <div class="admission">
    <div class="free"><b>FREE</b> <span>ADMISSION</span></div>
    <span class="vip">(VIP TICKETS AVAILABLE)</span>
  </div>

  <div class="hashtag">#loneprairiecanvasandsound</div>

  <div class="website">www.loneprairiecanvasandsoundjubilee.example</div>
</main>
</body>
</html>
```